Web Design for US Hispanic Business Community

Zap Kelo Network aka www.TalvoraMerca.TV is a dynamic new entrant in the the Hispanic internet small business solutions and services marketplace, through - engaging easy to use start-up business solutions.

Talvora Merca TV will feature a local online production of a weekly lifestyle show surrounded around community interest. Video news, business, Fashion and food channels and other topics around the Hispanic lifestyle trends in local Colorado area and across the US.

TMTV also provides budding Hispanic entrepreneurs a one stop shopping spot, providing access, participation and guidance including coaching, that may have been unattainable in the past, due to U.S job market shortages. For those Hispanics who want to to move into the business world and attain an improved and better quality of life.

To established sme's including e-commerce businesses and traditional retailers, TMTV will provide a platform from which to leverage Hispanic market share and brand positioning. Content on this site will also attract and engage Businesses, CEO's and budding entrepreneurs.

Solutions offered on Talvora Merca TV

Focused and tightly targeted Audience
Strategic Marketing Solutions (sem/seo/social media)
Education and Learning
Custom Content Creation
Product Placement
How to videos
Daily Deals
CEO Corner

Objective of this web portal: Talvora Merca TV will build a unique internet portal site, like no other and combind this with unique products and services that will guide both businesses and consumers to the site. This internet portal will be the the first point of contact for all those engaging in Talvora Merca TV and will be the point from which users start to interact with the portal. Ideally, this will be the first point from which Hispanics in the US start all internet activity.

Design Needs (Please note this is design only, Coding/development to be done by someone else):

I will be using a Wordpress CMS so please keep this in mind.

I'll be needing design for the following 4 main pages and the 5 "templates" below. I have attached the Logo to work with. Please note the font used in the circles can be customised if you think there is a better choice.

Web Portal must have
1) Customised Home Page (creative & Original layouts PLEASE!!!
2) Customised Marketplace page (This page highlights all the products and services on offer through the site)
3) Customised Entertainment and Dining Page (with a fashionable and funky icon. This page will drive high traffic)
4)A Community Upload Page - This will be user generated content, you could potentially use the circles of the logo to mark video content (there is also potential to use one or more of the coloured circles with a little video camera beside it)

Template layouts for 5 other following pages.

5 other pages include -

News Channel, Health and Lifestyle, Fashion, Food and Recipes and Daily Deals (This could be a plugin but I'd probably still want it customised).

I have included here example of web layout I like, esp for home page(Brisk Parlor TV) http://briskparlor.tv/video-library/brisk-parlor-june-25-2012

I have attached a design map of home page design I like.

I have attached a flow chart on the content that will be uploaded on each page (Take note where RSS feeds fit in)

I have included in 'Nice to have' a link of a 'slide' that I would also like on the home page http://quillmarket.net/item/community/512734?WT.ac=category_thumb&WT.seg_1=category_thumb&WT.z_author=pebblork

Please see all attached documents and links included.

I need to see original layout concepts, Please!!!

Please make header logo Dominant...I also added an image that I think would look cool for the blogging images...

Added a couple new logo files please replace with this one. lso I created a logo for my UGC Video upload, that needs to be featured in middle of page and on the footer

Target Market(s)

25- 49 year old U.S Hispanics and those in business. Hispanic communities usage rates of Smartphones, Television, Online Video and Social networking and other forms of entertainment make this group one of todays most engaged populations in todays digital space. Following Trends of this group mean that according to Garvik reasecrh this group send 941 txt msgs a month, more then any other ethnic group and are 25% more likely to follow a brand and 18% more likely to follow a celebrity then any other online group.

Industry/Entity Type

E-Commerce

Requirements
Must have
• Must have a corporate, Tech savvy design feel (not over the top). This is a professional, but hip and fashionable site.
White Background
The ability to fit RSS video Feeds
Entertainment and Dining page must have radio box or a cool icon to customize it as fashionable entertainment page, as this page will land majority traffic.
SEE FLOW CHART ON WEB LAYOUT ATTACHED
Nice to have
• Experiment with the text color in slogan line, & font style in circles of logo.
Homepage including Slider (I have below is a link to a website that I am happy with the look of the slider on)
http://quillmarket.net/item/community/512734?WT.ac=category_thumb&WT.seg_1=category_thumb&WT.z_author=pebblork
Should not have
• Must not be cartoony or childish

6/27 Update,
I uploaded a image of slider I like at lumatrova.com (video tab,check it out)I love the functionality of it-this is hm pg screen we need wow factor!, I need banners on each side if possible or a creative way to find some banner ad space. I also uploaded TMTV Logo B Colors file try using the 1st image at top of page, need to see examples with this logo as well!

```html
<!DOCTYPE html>
<html lang="en">
<head>
<meta charset="utf-8">
<title>TalvoraMerca.TV</title>
<link href="https://fonts.googleapis.com/css2?family=Open+Sans:wght@400;600;700;800&display=swap" rel="stylesheet">
<style>
:root{
  --page:#f4f3f1;
  --white:#ffffff;
  --ink:#3d3d3d;
  --muted:#8a8a8a;
  --rule:#dcdcdc;
  --brown:#6b5b4b;
  --olive:#8c7c52;
  --teal:#3e6a62;
  --teal-bright:#1ea3a0;
  --red:#c8312c;
  --red-bright:#e0342b;
  --purple:#8d4fa5;
  --green:#6aa84f;
  --orange:#e58a1f;
  --pink:#e4007c;
  --banner:#ddd5b3;
  --banner-edge:#c7bb8e;
  --panel:#efefef;
  --footer:#e7e4df;
}
*{box-sizing:border-box;margin:0;padding:0}
html,body{width:1200px;height:2503px;overflow:hidden}
body{position:relative;background:var(--page);font-family:"Open Sans",Arial,sans-serif;color:var(--ink);font-size:12px;line-height:1.45}
.abs{position:absolute}
.stripes{left:0;width:1200px;height:8px;background:repeating-linear-gradient(90deg,#c8312c 0 18px,#e58a1f 18px 36px,#6aa84f 36px 54px,#3e6a62 54px 72px,#8d4fa5 72px 90px,#6b5b4b 90px 108px)}
.sheet{left:112px;top:8px;width:976px;height:2239px;background:var(--white)}

.brand{left:130px;top:30px;display:flex;align-items:center;gap:10px}
.brand-dot{width:40px;height:40px;border-radius:50%;background:var(--orange)}
.brand-name{font-size:30px;font-weight:700;color:var(--brown);letter-spacing:-.5px}
.ad-banner{background:var(--banner);border:1px solid var(--banner-edge);display:flex;align-items:center;justify-content:center;font-size:12px;color:#6d6650;letter-spacing:.3px}
.search{left:862px;top:86px;display:flex;gap:6px}
.search-field{width:140px;height:22px;border:1px solid #c9c9c9;font-size:10px;color:#aaa;padding:3px 6px;background:#fff}
.search-btn{width:60px;height:22px;border:1px solid #bdbdbd;background:linear-gradient(#fafafa,#e3e3e3);font-size:11px;text-align:center;line-height:20px}

.ticker{left:130px;top:121px;width:938px;height:30px;border:1px solid var(--rule);display:flex;align-items:center;font-size:10.5px;background:#fff}
.ticker-label{height:100%;display:flex;align-items:center;gap:6px;padding:0 14px;background:linear-gradient(#f7f7f7,#e8e8e8);font-weight:700;font-size:11.5px;color:#555;border-right:1px solid var(--rule)}
.ticker-item{padding:0 14px;color:#666;white-space:nowrap}
.ticker-item b{color:var(--teal);margin-right:8px}

.nav{left:130px;top:159px;width:938px;height:36px;background:#f2f2f2;border-bottom:3px solid var(--brown);display:flex}
.nav a{font-size:11.5px;font-weight:700;color:#555;text-decoration:none;padding:0 17px;line-height:33px;white-space:nowrap}
.nav a.is-active{background:var(--brown);color:#fff}

.spot-bar{left:130px;top:209px;width:938px;height:21px;background:var(--teal);color:#fff;font-weight:700;font-size:11px;padding-left:8px;line-height:21px}
.spot-track{left:130px;top:232px;width:938px;height:104px;background:var(--panel)}
.spot-thumb{top:251px;width:142px;height:68px;border:3px solid #fff;box-shadow:0 1px 4px rgba(0,0,0,.3)}

.hero{left:130px;top:356px;width:657px;height:234px;background:linear-gradient(100deg,#4a2e1c 0%,#8a5a37 35%,#d8b07a 60%,#c2936a 80%,#6f4a31 100%)}
.hero-copy{left:140px;top:378px;width:250px;color:#fff;font-size:10.5px;line-height:1.5}
.hero-copy h2{color:#f4a11d;font-size:15px;line-height:1.3;margin-bottom:6px;font-weight:700}
.hero-arrows{left:414px;top:552px;display:flex;gap:2px}
.hero-arrows span{width:34px;height:24px;background:#1c1c1c;display:flex;align-items:center;justify-content:center}

.gig-ad{left:806px;top:356px;width:262px;height:234px;background:linear-gradient(160deg,#d8342a,#a91f1a)}
.gig-name{left:818px;top:362px;color:#fff;font-size:22px;font-weight:700}
.gig-art{left:930px;top:362px;width:128px;height:170px;background:linear-gradient(#e9d24a,#c79b22);border-radius:8px}
.gig-head{left:818px;top:418px;color:#fff;font-size:25px;line-height:1.08;font-weight:800;width:112px}
.gig-cta{left:946px;top:542px;width:112px;height:34px;background:#f6c71b;color:#2b2b2b;font-size:15px;font-weight:700;display:flex;align-items:center;justify-content:center;border-radius:3px}

.sec-title{font-size:12px;font-weight:700;color:#4a4a4a;display:flex;align-items:center;gap:6px;border-bottom:1px solid var(--rule);padding-bottom:5px}
.sec-title .chev{font-size:14px;letter-spacing:-3px}
.rss{width:12px;height:12px;background:var(--orange);border-radius:2px;position:absolute}

.blog-card{top:645px;width:140px}
.blog-img{height:64px;border:3px solid #fff;box-shadow:0 1px 3px rgba(0,0,0,.3);position:relative}
.blog-img span{position:absolute;left:0;right:0;bottom:0;background:rgba(0,0,0,.6);color:#fff;font-size:10px;font-weight:700;padding:1px 5px}
.blog-card p{font-size:10.5px;color:#444;margin-top:4px;line-height:1.35}

.side-tabs{left:806px;top:620px;width:262px;height:22px;display:flex;border-bottom:2px solid #ddd}
.side-tabs span{font-size:10.5px;color:#777;padding:0 10px;line-height:20px}
.side-tabs span.is-active{color:var(--teal);font-weight:700;border-bottom:2px solid var(--teal)}
.side-list{left:806px;top:644px;width:262px;height:476px;background:var(--panel);padding:12px 10px}
.side-item{display:flex;gap:12px;height:92px;border-bottom:1px solid #dcdcdc;padding-top:8px}
.side-thumb{width:48px;height:48px;border:3px solid #fff;flex:none;background:linear-gradient(#8b8b8b,#4e4e4e)}
.side-item p{font-size:10.5px;color:#555;line-height:1.4}
.side-item small{display:block;font-size:9px;color:var(--muted);margin-top:3px}

.box{background:#fff;border:1px solid var(--rule)}
.tabs{display:flex;height:24px;font-size:10.5px;font-weight:700;color:#555}
.tabs span{padding:0 10px;line-height:24px;white-space:nowrap}
.tabs .is-active{color:#fff}
.list{list-style:none}
.list li{font-size:11px;color:#555;padding:7px 0 7px 18px;border-bottom:1px solid #ececec;position:relative;white-space:nowrap}
.list li::before{content:"";position:absolute;left:2px;top:11px;width:9px;height:9px;border-radius:50%;border:1px solid #aaa;background:#f4f4f4}
.meta{font-size:9.5px;color:var(--muted)}

.vote{left:142px;top:1006px;width:292px;height:128px;border:1px solid var(--rule)}
.vote-title{color:var(--pink);font-weight:700;font-size:11.5px;padding:4px 10px;background:#f6f6f6;border-bottom:1px solid var(--rule)}
.vote-thumb{left:12px;top:36px;width:66px;height:66px;border:3px solid #fff;box-shadow:0 1px 3px rgba(0,0,0,.35);background:linear-gradient(#c9a27a,#7a5a44)}
.vote-q{left:92px;top:34px;width:190px;font-size:11px;font-weight:600;color:#555}
.vote-opts{left:92px;top:76px;display:flex;align-items:center;gap:10px;font-size:11px}
.vote-btn{background:var(--pink);color:#fff;font-weight:700;font-size:10px;padding:2px 12px;margin-left:22px}

.health-item{left:487px;width:290px;height:150px}
.health-icon{left:0;top:6px;width:72px;height:74px;border:1px solid #ddd;background:linear-gradient(#f7f7f7,#dedede)}
.health-title{left:86px;top:0;font-size:11px;font-weight:700;color:#333;line-height:1.35;width:198px}
.health-date{left:86px;top:46px}
.health-body{left:86px;top:72px;font-size:10.5px;color:#555;line-height:1.5;width:198px}

.video{left:142px;top:1228px;width:292px;height:220px;background:linear-gradient(120deg,#d8dde3,#9aa3ad 50%,#5a6470)}
.play{left:258px;top:1300px;width:60px;height:60px;border-radius:50%;background:var(--red-bright);border:3px solid #fff}
.video-bar{left:142px;top:1430px;width:292px;height:18px;background:#1b1b1b}

.deal-new{left:473px;top:1192px;width:36px;height:14px;background:var(--red-bright);color:#fff;font-size:9px;font-weight:700;text-align:center;line-height:14px}
.deal-img{left:490px;top:1210px;width:136px;height:110px;background:linear-gradient(#fafafa,#e6e0dc);border:1px solid #eee}
.deal-price{left:636px;top:1263px;color:var(--red-bright);font-size:30px;font-weight:700}
.buy-badge{left:716px;top:1258px;width:50px;height:50px;border-radius:50%;background:var(--teal-bright);color:#fff;font-size:9.5px;font-weight:800;text-align:center;line-height:1.1;padding-top:14px}
.deal-table{left:487px;top:1342px;width:290px;display:flex;justify-content:space-between;font-size:10.5px;color:#555;border-top:1px solid #eee;padding-top:6px}
.deal-table div{text-align:center}
.cards{left:493px;top:1398px;display:flex;gap:3px}
.cards i{width:18px;height:11px;border-radius:1px}
.deal-hl{left:480px;top:1430px;width:300px;height:20px;background:linear-gradient(#f4f4f4,#e1e1e1);font-size:10.5px;font-weight:700;padding:2px 8px;display:flex;justify-content:space-between}
.deal-hl a{color:var(--pink);text-decoration:none;font-weight:600}

.subscribe{left:806px;top:1162px;width:262px;height:262px;background:#fff;border:5px solid transparent;border-image:repeating-linear-gradient(45deg,#d03b34 0 8px,#fff 8px 14px,#3d78b6 14px 22px,#fff 22px 28px) 5}
.sub-title{left:822px;top:1174px;font-size:24px;font-weight:600;color:#3f8ea8}
.sub-text{left:822px;top:1216px;width:232px;font-size:11px;color:#666;line-height:1.4}
.check{width:13px;height:13px;border:1px solid #999;background:#fff;display:inline-block;vertical-align:middle;margin-right:8px}
.sub-row{left:822px;font-size:11px;color:#555}
.sub-btn{top:1374px;height:22px;color:#fff;font-size:11px;font-weight:600;display:flex;align-items:center;justify-content:center}

.ent-item{left:142px;width:632px}
.ent-line{background:#efefef;font-size:11px;color:#555;padding:4px 10px;margin-top:4px}
.ent-line b{color:var(--red);margin-right:4px}

.feat{display:flex;gap:12px}
.feat-thumb{width:64px;height:64px;border:3px solid #fff;box-shadow:0 1px 3px rgba(0,0,0,.35);flex:none}
.feat p{font-size:11px;font-weight:700;color:#333;line-height:1.35}

.footer{left:0;top:2247px;width:1200px;height:256px;background:var(--footer)}
.foot-head{font-size:11px;font-weight:700;color:#b5651d}
.foot-thumb{top:2308px;width:88px;height:50px;border:3px solid #fff;box-shadow:0 1px 2px rgba(0,0,0,.3);background:linear-gradient(#7f7f7f,#3e3e3e)}
.foot-cap{top:2366px;width:90px;font-size:10px;color:#555;line-height:1.35}
.foot-links{list-style:none;font-size:10.5px;color:#555}
.foot-links li{height:26px}
.social li{display:flex;align-items:center;gap:8px}
.social i{width:12px;height:12px;border-radius:2px;display:inline-block}
.foot-search{left:914px;top:2284px;width:154px;height:22px;border-radius:11px;background:#d2d0cc;font-size:10px;color:#777;padding:3px 12px}
.foot-brand{left:914px;top:2360px;display:flex;align-items:center;gap:6px}
.foot-brand .brand-dot{width:22px;height:22px}
.foot-brand span{font-size:16px;font-weight:700;color:var(--brown)}
.copy{left:130px;top:2443px;font-size:10px;color:#b5651d;line-height:1.7}
</style>
</head>
<body>

<div class="abs stripes" style="top:0"></div>
<div class="abs sheet"></div>

<header>
  <div class="abs brand"><span class="brand-dot"></span><span class="brand-name">TalvoraMerca.TV</span></div>
  <div class="abs ad-banner" style="left:628px;top:17px;width:440px;height:55px">ADD BANNER 468 X 60</div>
  <div class="abs search"><div class="search-field">Seekly Custom Search</div><div class="search-btn">Search</div></div>

  <div class="abs ticker">
    <div class="ticker-label">
      <svg width="14" height="12" viewBox="0 0 14 12"><path d="M1 11 L5 6 L8 8 L13 1" stroke="#c8312c" stroke-width="2" fill="none"/></svg>
      STOCK MARKET UPDATES
    </div>
    <div class="ticker-item"><b>UP CLOSE</b>| &nbsp;Aliquam vel velit at dictum bibendum nisl rhoncus.</div>
    <div class="ticker-item"><b>UP CLOSE</b>| &nbsp;Proin porta imperdiet urna, non lobortis lectus consectetur.</div>
  </div>

  <nav class="abs nav">
    <a class="is-active" href="#">NEWS CHANNELS</a>
    <a href="#">HEALTH &amp; SALUD!</a>
    <a href="#">FASHION/LIFESTYLE</a>
    <a href="#">MARKETPLACE</a>
    <a href="#">ENTERTAINMENT/DINING</a>
    <a href="#">FOOD RECIPIES</a>
    <a href="#">DAILY DEALS</a>
  </nav>
</header>

<section>
  <div class="abs spot-bar">SPOTLIGHT</div>
  <div class="abs spot-track"></div>
  <svg class="abs" style="left:140px;top:250px" width="16" height="66" viewBox="0 0 16 66"><path d="M14 2 L3 33 L14 64" stroke="#bbb" stroke-width="3" fill="none"/></svg>
  <svg class="abs" style="left:1044px;top:250px" width="16" height="66" viewBox="0 0 16 66"><path d="M2 2 L13 33 L2 64" stroke="#bbb" stroke-width="3" fill="none"/></svg>
  <div class="abs spot-thumb" style="left:180px;background:linear-gradient(120deg,#d8b7a0,#8a5b66)" role="img" aria-label="Spotlight photo of friends shopping"></div>
  <div class="abs spot-thumb" style="left:356px;background:linear-gradient(120deg,#c9d0d6,#7d8a96)" role="img" aria-label="Spotlight portrait photo"></div>
  <div class="abs spot-thumb" style="left:530px;background:linear-gradient(120deg,#e07a3a,#8a2d1a)" role="img" aria-label="Spotlight photo of a movie viewer"></div>
  <div class="abs spot-thumb" style="left:706px;background:linear-gradient(120deg,#c6b6a8,#6f5c50)" role="img" aria-label="Spotlight portrait photo"></div>
  <div class="abs spot-thumb" style="left:880px;background:linear-gradient(120deg,#d7a37a,#7d4b32)" role="img" aria-label="Spotlight photo of a child"></div>
</section>

<section>
  <div class="abs hero" role="img" aria-label="Slider photo of a fashion model in sunglasses"></div>
  <div class="abs hero-copy">
    <h2>Neque porro quisquam est quior ipsum quia dolor sit amet</h2>
    <p>Lorem Ipsum is simply dummy text of the printing and typesetting industry. Lorem Ipsum has been industry's standard dummy text ever since the 1500s, when an unknown printer took a galley of type and scrambled it to make a type specimen book. It has survived not only five centuries.</p>
  </div>
  <div class="abs hero-arrows">
    <span><svg width="10" height="12" viewBox="0 0 10 12"><path d="M8 1 L2 6 L8 11" stroke="#fff" stroke-width="2" fill="none"/></svg></span>
    <span><svg width="10" height="12" viewBox="0 0 10 12"><path d="M2 1 L8 6 L2 11" stroke="#fff" stroke-width="2" fill="none"/></svg></span>
  </div>

  <div class="abs gig-ad"></div>
  <div class="abs gig-art" role="img" aria-label="Advertisement mascot illustration"></div>
  <div class="abs gig-name">Gigbarn</div>
  <div class="abs gig-head">WOW! Skilled help from $5</div>
  <div class="abs gig-cta">Check it out</div>
</section>

<section>
  <div class="abs sec-title" style="left:130px;top:604px;width:657px">RECENT BLOG ROLL <span class="chev">››</span></div>
  <div class="abs blog-card" style="left:130px"><div class="blog-img" style="background:linear-gradient(#d5c2b0,#8b6f5a)" role="img" aria-label="Blog photo of a family"><span>Lorem Lipsum</span></div><p>Lorem Ipsum is simply dummy printing text...</p></div>
  <div class="abs blog-card" style="left:302px"><div class="blog-img" style="background:linear-gradient(#e2d3c4,#a08878)" role="img" aria-label="Blog photo of friends"><span>Lorem Lipsum</span></div><p>Lorem Ipsum is simply dummy printing text...</p></div>
  <div class="abs blog-card" style="left:475px"><div class="blog-img" style="background:linear-gradient(#d8c7b8,#7d6a5c)" role="img" aria-label="Blog photo of a couple"><span>Lorem Lipsum</span></div><p>Lorem Ipsum is simply dummy printing text...</p></div>
  <div class="abs blog-card" style="left:647px"><div class="blog-img" style="background:linear-gradient(#6d7786,#232a33)" role="img" aria-label="Blog photo of a performer on stage"><span>Lorem Lipsum</span></div><p>Lorem Ipsum is simply dummy printing text...</p></div>
</section>

<aside>
  <div class="abs side-tabs"><span class="is-active">POPULAR</span><span>RECENT</span><span>COMMENTS</span><span>TAGS</span></div>
  <div class="abs side-list">
    <div class="side-item"><div class="side-thumb" role="img" aria-label="Article thumbnail"></div><p>Roto iustum eum laoreet tation sapien, et tristique. ulla m eum laoreet tation...<small>Jul 29, 2012 · 1 comment(s)</small></p></div>
    <div class="side-item"><div class="side-thumb" role="img" aria-label="Article thumbnail"></div><p>Roto iustum eum laoreet tation sapien, et tristique. ulla m eum laoreet tation...<small>Jul 29, 2012 · 1 comment(s)</small></p></div>
    <div class="side-item"><div class="side-thumb" role="img" aria-label="Article thumbnail"></div><p>Roto iustum eum laoreet tation sapien, et tristique. ulla m eum laoreet tation...<small>Jul 29, 2012 · 1 comment(s)</small></p></div>
    <div class="side-item"><div class="side-thumb" role="img" aria-label="Article thumbnail"></div><p>Roto iustum eum laoreet tation sapien, et tristique. ulla m eum laoreet tation...<small>Jul 29, 2012 · 1 comment(s)</small></p></div>
    <div class="side-item" style="border:0"><div class="side-thumb" role="img" aria-label="Article thumbnail"></div><p>Roto iustum eum laoreet tation sapien, et tristique. ulla m eum laoreet tation...<small>Jul 29, 2012 · 1 comment(s)</small></p></div>
  </div>
</aside>

<section>
  <div class="abs sec-title" style="left:130px;top:786px;width:316px;border:0">NEWS <span class="chev">››</span></div>
  <span class="rss" style="left:432px;top:790px"></span>
  <div class="abs box" style="left:130px;top:812px;width:316px;height:329px"></div>
  <div class="abs tabs" style="left:130px;top:812px;width:316px;border-bottom:2px solid var(--olive)"><span class="is-active" style="background:var(--olive)">NATIONAL NEWS</span><span>LOCAL NEWS</span></div>
  <ul class="abs list" style="left:142px;top:842px;width:292px">
    <li>Integer non neque sapien, et tristique...</li>
    <li>Nam placerat leo et diam porttitor et lorem...</li>
    <li>Mauris mollis molestie mi, eu malesuadabus vel...</li>
    <li>Integer non neque sapien, et tristique...</li>
    <li style="border:0">Nam placerat leo et diam porttitor et lorem...</li>
  </ul>
  <div class="abs vote">
    <div class="vote-title">Vote Now!</div>
    <div class="abs vote-thumb" role="img" aria-label="Poll photo of a couple"></div>
    <div class="abs vote-q">Neque porro quisquam est qui dolo quia dolor sit amet?</div>
    <div class="abs vote-opts"><span>◉ Yes</span><span>○ No</span><span class="vote-btn">VOTE</span></div>
  </div>
</section>

<section>
  <div class="abs sec-title" style="left:473px;top:786px;width:314px;border:0">HEALTH <span class="chev">››</span></div>
  <span class="rss" style="left:773px;top:790px"></span>
  <div class="abs box" style="left:473px;top:812px;width:314px;height:329px"></div>
  <div class="abs health-item" style="top:826px">
    <div class="abs health-icon" role="img" aria-label="Heart and stethoscope illustration"></div>
    <div class="abs health-title">Roto iustum eum laoreet tation sapien, et tristique. ulla...</div>
    <div class="abs health-date meta">Jul 29, 2012 · 1 comment(s)</div>
    <div class="abs health-body">Elit prem moss commodo lobortis. Abluo verear amet velit Humo ncsi mpu abbas bladius dolore qui dolo rem ipsum quia dolor sit amet...</div>
  </div>
  <div class="abs health-item" style="top:990px">
    <div class="abs health-icon" role="img" aria-label="Heart and stethoscope illustration"></div>
    <div class="abs health-title">Roto iustum eum laoreet tation sapien, et tristique. ulla...</div>
    <div class="abs health-date meta">Jul 29, 2012 · 1 comment(s)</div>
    <div class="abs health-body">Elit prem moss commodo lobortis. Abluo verear amet velit Humo ncsi mpu abbas bladius doloreit amet...</div>
  </div>
</section>

<section>
  <div class="abs sec-title" style="left:130px;top:1168px;width:316px;border:0">MARKET PLACE <span class="chev">››</span></div>
  <div class="abs box" style="left:130px;top:1192px;width:316px;height:343px"></div>
  <div class="abs tabs" style="left:130px;top:1192px;width:316px;border-bottom:2px solid var(--olive)"><span class="is-active" style="background:var(--olive)">HOW TO VIDEOS</span><span>BUSINESS SULUTIONS</span></div>
  <div class="abs video" role="img" aria-label="Video still of a businessman in an office"></div>
  <div class="abs play"></div>
  <svg class="abs" style="left:282px;top:1318px" width="18" height="24" viewBox="0 0 18 24"><path d="M0 0 L18 12 L0 24 Z" fill="#fff"/></svg>
  <div class="abs video-bar"></div>
  <svg class="abs" style="left:148px;top:1434px" width="280" height="10" viewBox="0 0 280 10"><path d="M0 1 L7 5 L0 9 Z" fill="#fff"/><rect x="16" y="4" width="170" height="2" fill="#555"/><rect x="16" y="4" width="48" height="2" fill="#e0342b"/><circle cx="64" cy="5" r="4" fill="#ddd"/><rect x="250" y="2" width="10" height="6" fill="#bbb"/><rect x="266" y="2" width="12" height="6" fill="none" stroke="#bbb"/></svg>
  <div class="abs" style="left:142px;top:1456px;width:292px;font-size:11px;font-weight:700;color:#333;line-height:1.35">Euismod Sudo Autem Adipiscing Abdo Loquor Velit Molior Augue...</div>
  <div class="abs meta" style="left:142px;top:1500px">Jul 29, 2012 · 1 comment(s)</div>
</section>

<section>
  <div class="abs sec-title" style="left:473px;top:1168px;width:314px;border:0">DAILY DEALS <span class="chev">››</span></div>
  <div class="abs box" style="left:473px;top:1192px;width:314px;height:343px"></div>
  <div class="abs deal-img" role="img" aria-label="Product photo of brown sunglasses"></div>
  <div class="abs deal-new">NEW</div>
  <div class="abs" style="left:636px;top:1204px;font-size:11.5px;font-weight:700;color:#333">Orin OS-013 Sunglasses</div>
  <div class="abs meta" style="left:636px;top:1230px">Time Left To Buy : 21 : 4 : 10</div>
  <div class="abs deal-price">$50</div>
  <div class="abs buy-badge">BUY<br>NOW!</div>
  <div class="abs deal-table">
    <div>Actual Price:<br><s>$100</s></div>
    <div>Offer Price:<br>$ 50</div>
    <div>Discount:<br><span style="color:var(--red-bright);font-weight:700">50%</span></div>
  </div>
  <div class="abs cards"><i style="background:#1b4f9c"></i><i style="background:#e89b1c"></i><i style="background:#2a7fc1"></i><i style="background:#7fb3d6"></i><i style="background:#d23a2f"></i></div>
  <div class="abs deal-hl">Deal Highlights : <a href="#">+More</a></div>
  <ul class="abs list" style="left:480px;top:1452px;width:296px">
    <li>Unisex Eyewear</li>
    <li style="border:0">Color: Brownish Red</li>
  </ul>
</section>

<aside>
  <div class="abs subscribe"></div>
  <div class="abs sub-title">Subscribe</div>
  <svg class="abs" style="left:1018px;top:1176px" width="34" height="26" viewBox="0 0 34 26"><rect x="1" y="5" width="30" height="19" fill="#fff" stroke="#999" transform="rotate(-8 16 14)"/><path d="M3 6 L16 16 L30 2" stroke="#999" fill="none" transform="rotate(-8 16 14)"/></svg>
  <div class="abs sub-text">Select the newsletter(s) to which you want to subscribe or unsubscrib.</div>
  <div class="abs sub-row" style="top:1266px"><span class="check" style="text-align:center;font-size:10px;line-height:11px">✓</span>Newsletters</div>
  <div class="abs sub-row" style="top:1300px;display:flex;align-items:center"><span class="check"></span><span class="brand-dot" style="width:18px;height:18px;margin-right:6px"></span><span style="font-size:14px;font-weight:700;color:var(--brown)">TalvoraMerca.TV</span></div>
  <div class="abs sub-btn" style="left:822px;width:80px;background:#eea12a">Subscribe</div>
  <div class="abs sub-btn" style="left:925px;width:90px;background:var(--red-bright)">Unsubscribe</div>
</aside>

<section>
  <div class="abs sec-title" style="left:130px;top:1560px;width:657px;border:0">ENTERTAINMENT / DINING <span class="chev">››</span></div>
  <div class="abs box" style="left:130px;top:1585px;width:657px;height:274px"></div>
  <div class="abs tabs" style="left:130px;top:1585px;width:657px;border-bottom:2px solid var(--red)"><span class="is-active" style="background:var(--red)">"NIGHT SCEN" RESTAURANT &amp; NIGHTCLUB REVIESS</span><span style="margin-left:12px">"LOCAL" EVENT CALENDAR</span><span style="margin-left:12px">HOW TO VIDEOS</span></div>
  <span class="rss" style="left:770px;top:1590px"></span>
  <div class="abs ent-item" style="top:1620px"><div class="meta">Jul 29, 2012 · 1 comment(s)</div><div class="ent-line"><b>MONEY</b>: Aptent roto cogo quidne paratus paratus abico neo aptent...</div></div>
  <div class="abs ent-item" style="top:1678px"><div class="meta">Jul 29, 2012 · 1 comment(s)</div><div class="ent-line"><b>PEOPLE</b>: Aliquam consequat abico gentilis luptatum virtus singularis...</div></div>
  <div class="abs ent-item" style="top:1736px"><div class="meta">Jul 29, 2012 · 1 comment(s)</div><div class="ent-line"><b>MEDIA</b>: Zelus feugiat te olim obruo facilisis quadrum proprius gravis...</div></div>
  <div class="abs ent-item" style="top:1794px"><div class="meta">Jul 29, 2012 · 1 comment(s)</div><div class="ent-line"><b>TRAVEL</b>: Bene ideo commoveo quadrum abbas vero macto neo iugis ut iusto...</div></div>
</section>

<section>
  <div class="abs sec-title" style="left:130px;top:1886px;width:316px;border:0">FASHION / LIFESTYLE <span class="chev">››</span></div>
  <div class="abs box" style="left:130px;top:1910px;width:316px;height:215px"></div>
  <div class="abs tabs" style="left:130px;top:1910px;width:316px;border-bottom:2px solid var(--purple)"><span class="is-active" style="background:var(--purple)">BEAUTY &amp; FASHION TIPS</span><span>HOW TO VIDEOS</span></div>
  <div class="abs feat" style="left:146px;top:1952px;width:290px"><div class="feat-thumb" style="background:linear-gradient(#e3b97d,#9a6a3c)" role="img" aria-label="Beauty photo of a woman"></div><div><p>Roto iustum eum laoreet tation sapien, et tristique. ulla...</p><div class="meta" style="margin-top:6px">Jul 29, 2012 · 1 comment(s)</div></div></div>
  <ul class="abs list" style="left:142px;top:2030px;width:292px">
    <li>Integer non neque sapien, et tristique...</li>
    <li>Nam placerat leo et diam porttitor et lorem...</li>
    <li style="border:0">Mauris mollis molestie mi, eu malesuadabus vel...</li>
  </ul>
</section>

<section>
  <div class="abs sec-title" style="left:473px;top:1886px;width:314px;border:0">FOOD / RECIPIES <span class="chev">››</span></div>
  <span class="rss" style="left:773px;top:1890px"></span>
  <div class="abs box" style="left:473px;top:1910px;width:314px;height:215px;border-top:3px solid var(--green)"></div>
  <div class="abs feat" style="left:489px;top:1928px;width:290px"><div class="feat-thumb" style="background:linear-gradient(#e6e1d8,#b74a3a)" role="img" aria-label="Food photo of a dish"></div><div><p>Roto iustum eum laoreet tation sapien, et tristique. ulla...</p><div class="meta" style="margin-top:6px">Jul 29, 2012 · 1 comment(s)</div></div></div>
  <ul class="abs list" style="left:485px;top:2002px;width:292px">
    <li>Integer non neque sapien, et tristique...</li>
    <li>Nam placerat leo et diam porttitor et lorem...</li>
    <li>Mauris mollis molestie mi, eu malesuadabus vel...</li>
    <li style="border:0">Integer non neque sapien, et tristique...</li>
  </ul>
</section>

<div class="abs ad-banner" style="left:380px;top:2161px;width:440px;height:55px">ADD BANNER 468 X 60</div>

<footer>
  <div class="abs footer"></div>
  <div class="abs stripes" style="top:2247px"></div>
  <div class="abs foot-head" style="left:130px;top:2280px">MOST VIEWED</div>
  <div class="abs foot-thumb" style="left:136px" role="img" aria-label="Video thumbnail"></div>
  <div class="abs foot-thumb" style="left:235px" role="img" aria-label="Video thumbnail"></div>
  <div class="abs foot-thumb" style="left:335px" role="img" aria-label="Video thumbnail"></div>
  <div class="abs foot-thumb" style="left:433px" role="img" aria-label="Video thumbnail"></div>
  <div class="abs foot-cap" style="left:136px">Roto iustum eu am iugis laoreet tation...</div>
  <div class="abs foot-cap" style="left:235px">Roto iustum eu am iugis laoreet tation...</div>
  <div class="abs foot-cap" style="left:335px">Roto iustum eu am iugis laoreet tation...</div>
  <div class="abs foot-cap" style="left:433px">Roto iustum eu am iugis laoreet tation...</div>

  <div class="abs foot-head" style="left:587px;top:2280px">CONNECT WITH US</div>
  <ul class="abs foot-links" style="left:587px;top:2310px">
    <li>About us</li><li>Archive</li><li>Newsletters</li><li>Advertise</li><li>Contact</li>
  </ul>
  <div class="abs foot-head" style="left:765px;top:2280px">CONNECT WITH US</div>
  <ul class="abs foot-links social" style="left:765px;top:2310px">
    <li><i style="background:var(--orange)"></i>RSS</li>
    <li><i style="background:#4fb5e6"></i>Murmel</li>
    <li><i style="background:#3b5b98"></i>Kinloop</li>
    <li><i style="background:#1f72b0"></i>Proventa</li>
  </ul>
  <div class="abs foot-search">Search</div>
  <div class="abs foot-brand"><span class="brand-dot"></span><span>TalvoraMerca.TV</span></div>
  <div class="abs copy">Copyright © 2012 TalvoraMerca.TV . All Rights Reserved.<br>Privacy Policy &nbsp;|&nbsp; Sitemap</div>
</footer>

</body>
</html>
```